New Business Card Design Project

I need a clean, professional business card. I'd like it to have some color, but not be wild. We do technology consulting and we have clients large and small who trust us with some of their most important data and projects. Simple but not boring should drive all design proposals. Multicolored and two sided, but with a matte finish, I think.
For more on tone, check out our website: http://brindlequay.com

Target Market(s)

Upper management of respected businesses. Tech savvy, but not "hipster".

Industry/Entity Type

Business

Requirements
Must have
• Files need to be provided in .eps and in .pdf in a manner that allows for easy updates.
Must have Name, Title, Phone, Email, Twitter, Website
Nice to have
• Logo/Name shouldn't be too big. One thing I've read several places is that the bigger the logo, the smaller the brand. A good article on dos and don'ts here: http://www.mossvane.com/2011/02/business-card-experience.html

```html
<!DOCTYPE html>
<html lang="en">
<head>
<meta charset="utf-8">
<title>Brindle Quay — Business Card</title>
<link rel="stylesheet" href="https://fonts.googleapis.com/css2?family=Oxygen:wght@300;400&display=swap">
<style>
  :root {
    --backdrop: #e6e7e8;
    --card: #ffffff;
    --ink: #6d6e70;
    --ink-soft: #8a8b8d;
    --teal: #3a9fae;
    --lime: #8dbb2a;
    --sky: #36a9e1;
  }
  * { box-sizing: border-box; margin: 0; padding: 0; }
  html, body {
    width: 1200px; height: 900px; overflow: hidden;
    background: var(--backdrop);
    font-family: "Oxygen", "Helvetica Neue", Arial, sans-serif;
  }
  .stage {
    width: 1200px; height: 900px;
    display: flex; flex-direction: column;
    align-items: center; justify-content: center; gap: 56px;
  }
  .card {
    position: relative;
    width: 600px; height: 343px;
    background: var(--card);
    box-shadow: 0 6px 18px rgba(0,0,0,0.12);
  }
  /* Front */
  .brand {
    position: absolute; right: 48px; bottom: 62px;
    display: flex; align-items: center; gap: 14px;
  }
  .brand-mark { width: 22px; height: 22px; background: var(--lime); }
  .brand-name {
    font-weight: 300; font-size: 34px; letter-spacing: 3px;
    color: var(--ink-soft);
  }
  /* Back */
  .edge-band {
    position: absolute; left: 0; top: 0; bottom: 0; width: 70px;
    background: linear-gradient(90deg, var(--teal), #5bb6c2);
  }
  .person { position: absolute; left: 150px; top: 62px; }
  .person-name {
    font-weight: 400; font-size: 26px; letter-spacing: 1.5px;
    color: var(--ink);
  }
  .person-title { font-size: 15px; color: var(--ink); margin-top: 2px; }
  .contacts {
    position: absolute; left: 112px; top: 178px;
    list-style: none; display: flex; flex-direction: column; gap: 10px;
  }
  .contact {
    display: flex; align-items: center; gap: 16px;
    font-size: 17px; letter-spacing: 1px; color: var(--ink);
  }
  .contact svg { width: 18px; height: 18px; flex: none; }
</style>
</head>
<body>
<main class="stage">
  <section class="card card-front" aria-label="Card front">
    <div class="brand">
      <span class="brand-mark"></span>
      <span class="brand-name">BRINDLE QUAY</span>
    </div>
  </section>

  <section class="card card-back" aria-label="Card back">
    <div class="edge-band" role="img" aria-label="Teal dot-pattern band along the left edge"></div>
    <div class="person">
      <p class="person-name">DANA WHITLOW</p>
      <p class="person-title">CEO</p>
    </div>
    <ul class="contacts">
      <li class="contact">
        <svg viewBox="0 0 18 18" aria-hidden="true"><rect x="4" y="1" width="10" height="16" rx="1.5" fill="none" stroke="var(--lime)" stroke-width="1.8"/><line x1="7" y1="14" x2="11" y2="14" stroke="var(--lime)" stroke-width="1.6"/></svg>
        <span>1-800-555-0147, ext. 700</span>
      </li>
      <li class="contact">
        <svg viewBox="0 0 18 18" aria-hidden="true"><text x="9" y="14" text-anchor="middle" font-size="16" font-family="Oxygen, sans-serif" font-weight="700" fill="var(--teal)">@</text></svg>
        <span>dana@brindlequay.com</span>
      </li>
      <li class="contact">
        <svg viewBox="0 0 18 18" aria-hidden="true"><rect x="4" y="2" width="10" height="14" rx="5" fill="none" stroke="var(--lime)" stroke-width="1.6"/><line x1="9" y1="2" x2="9" y2="8" stroke="var(--lime)" stroke-width="1.4"/><line x1="4" y1="8" x2="14" y2="8" stroke="var(--lime)" stroke-width="1.4"/></svg>
        <span>www.brindlequay.com</span>
      </li>
      <li class="contact">
        <svg viewBox="0 0 18 18" aria-hidden="true"><circle cx="9" cy="9" r="7" fill="var(--sky)"/></svg>
        <span>@quaykeeper</span>
      </li>
    </ul>
  </section>
</main>
</body>
</html>
```